Stylish Business Card for Modern hair salon

I need a simple business card design using our salon logo and colours that are in the logo. We service clients of all ages but predominantly those in the 18 to 55 age range. We have a young staff and are looking to have a card that will present a modern and clean image that represents who we are. The card should be in black and white same as our logo. Minimal use of other colours is allowed.

Industry/Entity Type

Hair And Beauty

Contact Information for Business Card

The design should have the following information
salon name - TR Hair Studio
address - 2751 Birchfield Rd.E. Mississauga, ON L7P3K2
phone - 905 614-2870
website - trhairexample.ca
instagram - tr.hairstudio
twitter - @TR_HairStudio

Colors
000000
ffffff
474747

Requirements
Must have
• simple design, salon name, address, phone, website, instagram, twitter info
• Back of card should have the following:
• YOUR NEXT APPOINTMENT
• DATE
• TIME
Nice to have
• simple design, clear to see and read,
• predominantly black and white colour, minimal use of other colours is ok
Should not have
• many colours, various fonts

```html
<!DOCTYPE html>
<html lang="en">
<head>
<meta charset="utf-8">
<title>TR Hair Studio – Business Card</title>
<link rel="stylesheet" href="https://fonts.googleapis.com/css2?family=Questrial&display=swap">
<style>
  :root {
    --ink: #000000;
    --card: #1c1d1f;
    --paper: #ffffff;
    --muted: #474747;
    --stage: #e6e6e6;
  }
  * { box-sizing: border-box; margin: 0; padding: 0; }
  html, body { width: 1200px; height: 780px; overflow: hidden; }
  body {
    background: var(--stage);
    font-family: "Questrial", "Century Gothic", sans-serif;
    color: var(--paper);
    position: relative;
  }
  .card {
    position: absolute;
    width: 540px;
    height: 309px;
    background: var(--card);
    border-radius: 18px;
    overflow: hidden;
  }
  .card--back { left: 60px; top: 60px; }
  .card--front { left: 600px; top: 410px; }

  .wordmark {
    font-family: "Questrial", sans-serif;
    font-weight: 400;
    color: var(--paper);
    text-align: center;
    line-height: 1;
    white-space: nowrap;
  }
  .card--back .wordmark {
    position: absolute;
    left: 0; right: 0; top: 26px;
    font-size: 58px;
    letter-spacing: 6px;
  }

  .appointment {
    position: absolute;
    left: 18px; right: 18px; bottom: 18px;
    height: 178px;
    background: var(--paper);
    border-radius: 14px;
    color: var(--ink);
  }
  .appointment__title {
    position: absolute;
    top: 26px; left: 0; right: 0;
    text-align: center;
    font-size: 14px;
    letter-spacing: 1px;
  }
  .appointment__field {
    position: absolute;
    display: flex;
    align-items: flex-end;
    gap: 8px;
    font-size: 13px;
    letter-spacing: 0.5px;
  }
  .appointment__field .rule {
    border-bottom: 1px solid var(--ink);
    height: 14px;
  }
  .field--date { left: 26px; top: 72px; }
  .field--date .rule { width: 200px; }
  .field--time { right: 26px; top: 118px; }
  .field--time .rule { width: 220px; }

  .card--front .wordmark {
    position: absolute;
    left: 30px; top: 118px;
    width: 210px;
    font-size: 52px;
    letter-spacing: 5px;
  }
  .divider {
    position: absolute;
    left: 262px; top: 46px;
    width: 1px; height: 218px;
    background: #8a8a8a;
  }
  .contact {
    position: absolute;
    left: 286px; top: 66px;
    font-size: 14px;
    line-height: 1.45;
  }
  .contact__name { font-size: 19px; margin-bottom: 16px; letter-spacing: 0.3px; }
  .contact__row { display: flex; align-items: center; gap: 8px; }
  .contact__row svg { width: 13px; height: 13px; flex: none; }
</style>
</head>
<body>

  <section class="card card--back" aria-label="Appointment card">
    <div class="wordmark">TR HAIR</div>
    <div class="appointment">
      <p class="appointment__title">YOUR NEXT APPOINTMENT</p>
      <div class="appointment__field field--date"><span>DATE</span><span class="rule"></span></div>
      <div class="appointment__field field--time"><span>TIME</span><span class="rule"></span></div>
    </div>
  </section>

  <section class="card card--front" aria-label="Contact card">
    <div class="wordmark">TR HAIR</div>
    <div class="divider"></div>
    <div class="contact">
      <p class="contact__name">TR Hair Studio</p>
      <p>2751 Birchfield Rd.E.</p>
      <p>Mississauga, ON L7P3K2</p>
      <p class="contact__row">
        <svg viewBox="0 0 16 16" aria-hidden="true"><circle cx="8" cy="8" r="8" fill="#fff"/><path d="M5 4.5l1.6-.3.8 2-1 .8a5 5 0 002.6 2.6l.8-1 2 .8-.3 1.6c-3.5.3-6.8-3-6.5-6.5z" fill="#1c1d1f"/></svg>
        905 614-2870
      </p>
      <p class="contact__row">
        <svg viewBox="0 0 16 16" aria-hidden="true"><circle cx="8" cy="8" r="8" fill="#fff"/><circle cx="8" cy="8" r="4.5" fill="none" stroke="#1c1d1f" stroke-width="1"/><path d="M3.5 8h9M8 3.5c-2 2.5-2 6.5 0 9M8 3.5c2 2.5 2 6.5 0 9" fill="none" stroke="#1c1d1f" stroke-width="0.8"/></svg>
        trhairexample.ca
      </p>
      <p class="contact__row">
        <svg viewBox="0 0 16 16" aria-hidden="true"><circle cx="8" cy="8" r="8" fill="#fff"/></svg>
        tr.hairstudio
      </p>
      <p class="contact__row">
        <svg viewBox="0 0 16 16" aria-hidden="true"><circle cx="8" cy="8" r="8" fill="#fff"/></svg>
        @TR_HairStudio
      </p>
    </div>
  </section>

</body>
</html>
```